Northgate Process Solutions

8.5 x 11 flyer one or two sides is fine. This will be used for a trade show. See message for details

Target Market(s)

Refineries and Petrochemical plants

Industry/Entity Type

Oil

```html
<!DOCTYPE html>
<html lang="en">
<head>
<meta charset="utf-8">
<title>Northgate Process Solutions – Trade Show Flyer</title>
<link rel="stylesheet" href="https://fonts.googleapis.com/css2?family=Montserrat:wght@500;600;700;800;900&family=Questrial&family=Lato:wght@400;700;900&display=swap">
<style>
  :root{
    --backdrop:#58595b;
    --paper:#ffffff;
    --paper-soft:#f6f6f6;
    --green:#0d8a43;
    --green-bright:#0aa85a;
    --gold:#c98a35;
    --gold-light:#e0ae6a;
    --silver:#b8b8bb;
    --ink:#1e1e1e;
    --steel-1:#c9cdd2;
    --steel-2:#8b8f95;
    --blue-1:#1f5fc4;
    --blue-2:#0b2f78;
  }
  *{margin:0;padding:0;box-sizing:border-box}
  html,body{width:720px;height:1200px;overflow:hidden;background:var(--backdrop)}
  .canvas{position:relative;width:720px;height:1200px}
  .page{position:absolute;left:154px;width:413px;height:535px;background:var(--paper);overflow:hidden}
  .page--front{top:40px}
  .page--back{top:619px;background:var(--paper-soft)}
  .layer{position:absolute;left:0;top:0}

  /* front */
  .brand-box{position:absolute;left:7px;top:14px;width:114px;height:35px;background:var(--paper);display:flex;align-items:center;justify-content:center;gap:5px;box-shadow:0 1px 3px rgba(0,0,0,.25)}
  .brand-box__dot{width:7px;height:7px;border-radius:50%;background:var(--green)}
  .brand-box__name{font-family:"Montserrat",sans-serif;font-weight:800;font-size:7.6px;line-height:1.1;color:var(--ink);text-align:left}
  .headline{position:absolute;left:0;width:100%;text-align:center;font-family:"Montserrat",sans-serif}
  .headline--main{top:230px;font-size:20.5px;font-weight:800;color:var(--green);letter-spacing:.2px}
  .headline--sub{top:259px;font-family:"Questrial",sans-serif;font-size:12.5px;letter-spacing:2.2px;color:var(--ink)}
  .headline--cats{top:279px;font-size:11.2px;font-weight:700;color:var(--ink)}
  .materials{position:absolute;list-style:none;font-family:"Questrial",sans-serif;font-size:12.2px;color:var(--ink)}
  .materials li{height:21.5px;line-height:21.5px;position:relative;padding-left:10px}
  .materials li::before{content:"";position:absolute;left:0;top:8.5px;width:4.5px;height:4.5px;border-radius:50%;background:var(--ink)}
  .materials li.more::before{display:none}
  .materials--left{left:42px;top:313px}
  .materials--right{left:232px;top:313px}
  .materials-divider{position:absolute;left:206px;top:327px;width:1px;height:94px;background:var(--green)}
  .contact{position:absolute;left:0;width:100%;text-align:center;font-family:"Lato",sans-serif;color:var(--ink)}
  .contact--title{top:469px;font-size:9px;font-weight:900}
  .contact--phone{top:484px;font-size:9.5px;display:flex;justify-content:center;align-items:center;gap:2px}
  .footer-link{position:absolute;top:513px;font-family:"Lato",sans-serif;font-size:8.4px;color:#fff;display:flex;align-items:center;gap:3px}
  .footer-link--mail{left:12px}
  .footer-link--web{right:17px}

  /* back */
  .photo{position:absolute;left:0;width:100%}
  .photo--plant{top:0;height:151px;background:linear-gradient(180deg,#dfe2e6 0%,var(--steel-1) 45%,var(--steel-2) 100%)}
  .photo--drums{top:390px;height:145px;background:radial-gradient(ellipse at 50% 25%,#dfe9f5 0%,#6d9ad8 22%,var(--blue-1) 48%,var(--blue-2) 100%)}
  .section-title{position:absolute;top:158px;left:0;width:100%;text-align:center;font-family:"Montserrat",sans-serif;font-weight:900;font-size:20px;color:var(--green)}
  .intro{position:absolute;top:185px;left:20px;width:373px;text-align:center;font-family:"Montserrat",sans-serif;font-weight:500;font-size:7.1px;line-height:14.8px;color:var(--ink)}
  .tagline{position:absolute;left:0;width:100%;text-align:center;font-family:"Lato",sans-serif;font-weight:700;font-size:11.2px;color:var(--green);letter-spacing:-.2px}
  .tagline--one{top:278px}
  .tagline--two{top:297px}
  .years-badge{position:absolute;left:177px;top:321px;width:58px;height:59px}
  .years-badge__text{position:absolute;left:0;top:0;width:100%;height:100%;display:flex;flex-direction:column;align-items:center;justify-content:center;font-family:"Lato",sans-serif;font-weight:700;color:#fff;line-height:1}
  .years-badge__num{font-size:20px}
  .years-badge__label{font-size:12px;margin-top:2px}
  .follow{position:absolute;left:332px;top:494px;font-family:"Lato",sans-serif;font-weight:700;font-size:8.6px;color:#fff}
  .follow__icons{display:flex;gap:6px;margin-top:4px;padding-left:0}
  .follow__icons span{width:12px;height:12px;border-radius:50%;background:#fff;opacity:.9}
</style>
</head>
<body>
<div class="canvas">

  <!-- Front side -->
  <section class="page page--front">
    <svg class="layer" width="413" height="535" viewBox="0 0 413 535">
      <defs>
        <linearGradient id="skyRefinery" x1="0" y1="0" x2="0" y2="1">
          <stop offset="0" stop-color="#d7dde3"/>
          <stop offset=".6" stop-color="#9a9c9e"/>
          <stop offset="1" stop-color="#4d4b48"/>
        </linearGradient>
        <linearGradient id="goldFade" x1="0" y1="0" x2="1" y2="0">
          <stop offset="0" stop-color="var(--gold)"/>
          <stop offset="1" stop-color="var(--gold-light)"/>
        </linearGradient>
        <radialGradient id="oilPour" cx=".45" cy=".5" r=".6">
          <stop offset="0" stop-color="#e7c36a"/>
          <stop offset=".45" stop-color="#c9c9c9"/>
          <stop offset="1" stop-color="#6e5a40"/>
        </radialGradient>
      </defs>
      <rect role="img" aria-label="Photo of refinery towers and pipework against the sky" x="0" y="0" width="413" height="230" fill="url(#skyRefinery)"/>
      <path d="M0,96 C90,135 200,170 330,181 L413,181 L413,208 L300,206 C190,200 80,175 0,160 Z" fill="var(--green-bright)"/>
      <path d="M0,140 C60,165 150,190 240,205 L0,190 Z" fill="url(#goldFade)"/>
      <path d="M0,188 C70,150 160,170 413,252 L413,535 L0,535 Z" fill="var(--paper)"/>
      <path d="M85,155 C200,175 300,210 413,210 L413,216 C300,216 200,185 85,158 Z" fill="var(--silver)"/>
      <circle role="img" aria-label="Photo of golden oil pouring from a metal can" cx="262" cy="152" r="62" fill="url(#oilPour)" stroke="var(--gold)" stroke-width="4"/>
      <path d="M0,414 C70,480 150,520 215,535 L0,535 Z" fill="var(--green-bright)"/>
      <path d="M413,460 C340,500 250,520 150,535 L413,535 Z" fill="url(#goldFade)"/>
      <path d="M413,445 C340,490 250,515 150,530 L150,533 C250,519 340,495 413,455 Z" fill="var(--silver)"/>
    </svg>

    <div class="brand-box">
      <span class="brand-box__dot"></span>
      <span class="brand-box__name">Northgate<br>Process Solutions</span>
    </div>

    <h1 class="headline headline--main">YOUR STRATEGIC PARTNER</h1>
    <p class="headline headline--sub">FOR PRODUCTIVE SOLUTIONS</p>
    <p class="headline headline--cats">BY-PRODUCTS • CO-PRODUCTS • PROCESS RESIDUALS</p>

    <ul class="materials materials--left">
      <li>Alcohols</li>
      <li>Asphalt Flux</li>
      <li>Bitumen</li>
      <li>Crude Oil</li>
      <li>Distillation Residue</li>
      <li>Distressed Material</li>
    </ul>
    <div class="materials-divider"></div>
    <ul class="materials materials--right">
      <li>Fuels</li>
      <li>Glycols</li>
      <li>Petroleum Hydrocarbons</li>
      <li>Solvents</li>
      <li>Tank Bottoms</li>
      <li class="more">And More!</li>
    </ul>

    <p class="contact contact--title">CONTACT US</p>
    <p class="contact contact--phone">
      <svg width="8" height="9" viewBox="0 0 24 24"><path d="M6.6 10.8a15 15 0 0 0 6.6 6.6l2.2-2.2c.3-.3.7-.4 1-.2 1.1.4 2.3.6 3.6.6.6 0 1 .4 1 1V20c0 .6-.4 1-1 1A17 17 0 0 1 3 4c0-.6.4-1 1-1h3.5c.6 0 1 .4 1 1 0 1.3.2 2.5.6 3.6.1.3 0 .7-.2 1z" fill="var(--ink)"/></svg>
      555-014-2000
    </p>

    <p class="footer-link footer-link--mail">
      <svg width="7" height="6" viewBox="0 0 14 10"><rect x=".5" y=".5" width="13" height="9" fill="none" stroke="#fff"/><path d="M.5 .5 7 6l6.5-5.5" fill="none" stroke="#fff"/></svg>
      info@northgate-ps.com
    </p>
    <p class="footer-link footer-link--web">
      <svg width="7" height="7" viewBox="0 0 14 14"><circle cx="7" cy="7" r="6" fill="none" stroke="#fff"/><path d="M1 7h12M7 1c3 3 3 9 0 12M7 1c-3 3-3 9 0 12" fill="none" stroke="#fff"/></svg>
      www.northgate-ps.com
    </p>
  </section>

  <!-- Back side -->
  <section class="page page--back">
    <div class="photo photo--plant" role="img" aria-label="Photo of a refinery storage tank with overhead pipeline"></div>

    <h2 class="section-title">WHAT WE DO</h2>
    <p class="intro">Northgate process solutions utilizes a multi-faceted approach by supporting various manufacturers, refineries, blender/packagers and distributors by purchasing residual by-products, co-products, bottoms, off spec or out of date and surplus material. We truly pride ourselves on our ability to source your residual materials as a feedstock into a secondary market; thereby improving your bottom line and improving the sustainability of our environment. In addition, we also review waste material for reuse or recycle. Whether truck, rail or barge, Northgate is here to meet your needs.</p>

    <p class="tagline tagline--one">Procurement of Process Residuals and Off-Spec Material Worldwide</p>
    <p class="tagline tagline--two">Your Trusted Partner For</p>

    <div class="years-badge">
      <svg width="58" height="59" viewBox="0 0 58 59"><polygon points="29,0 58,15 58,44 29,59 0,44 0,15" fill="var(--green-bright)"/></svg>
      <div class="years-badge__text">
        <span class="years-badge__num">26</span>
        <span class="years-badge__label">Years!</span>
      </div>
    </div>

    <div class="photo photo--drums" role="img" aria-label="Photo of a worker walking between stacked blue oil drums"></div>

    <div class="follow">
      FOLLOW US
      <div class="follow__icons"><span></span><span></span><span></span></div>
    </div>
  </section>

</div>
</body>
</html>
```